Brochure Design Project

Color brochure with text, graphics, and photos. (I will provide the text). 4 pages of 8 1/2 X 11". This is a brochure about dental implants.
Attached is the text and logo for the brochure.

See new parameters and information on the brochure project.

Included in the brochure is our address: Briar Ridge Dental Care, 418 North Cedar Avenue, Briar Ridge, PA 17943.  717-829-4617.  www.briarridgedentalcare.example.

Martin R. Pike, D.M.D., M.A.G.D., F.I.C.O.I. (Attached is photo for brochure)file://localhost/Users/mrpdmd7/Pictures/iPhoto%20Library/Masters/2003/Office%20Pictures/Dr.%20Pike%202.jpg

Target Market(s)

Adults, primarily senior adults.

Industry/Entity Type

Dental

```html
<!DOCTYPE html>
<html lang="en">
<head>
<meta charset="utf-8">
<title>Briar Ridge Dental Care – Implant Brochure</title>
<link rel="stylesheet" href="https://fonts.googleapis.com/css2?family=Arimo:wght@400;700&family=Didact+Gothic&display=swap">
<style>
:root{
  --stage:#e3e3e3;
  --blue:#0f8fdc;
  --navy:#1c4f9c;
  --white:#ffffff;
  --ink:#2a2a2a;
  --logo-blue:#1f6aa8;
}
*{margin:0;padding:0;box-sizing:border-box}
html,body{width:1200px;height:721px;overflow:hidden;background:var(--stage)}
.canvas{position:relative;width:1200px;height:721px}
.spread{position:absolute;top:153px;height:416px;background:var(--white);overflow:hidden}
.spread--cover{left:53px;width:537px}
.spread--inside{left:597px;width:550px}

/* cover: back panel */
.back-panel{position:absolute;left:0;top:0;width:269px;height:416px;background:var(--blue)}
.back-panel__accent{position:absolute;left:0;top:345px;width:33px;height:71px;background:var(--navy)}
.contact{position:absolute;left:45px;top:321px;width:220px;color:var(--white);font-family:Arimo,sans-serif;font-size:10px;line-height:10.8px;font-style:normal}
.contact__name{font-weight:700;margin-bottom:12px}
.contact__url{position:absolute;left:45px;top:393px;color:var(--white);font-family:Arimo,sans-serif;font-size:10px;line-height:12px}

/* cover: front panel */
.front-panel{position:absolute;left:269px;top:0;width:268px;height:416px}
.brand{position:absolute;left:0;top:40px;width:268px;display:flex;flex-direction:column;align-items:center;gap:6px}
.brand__dot{width:18px;height:18px;border-radius:50%;background:var(--logo-blue)}
.brand__name{font-family:Arimo,sans-serif;font-weight:700;font-size:11px;color:var(--logo-blue);letter-spacing:.5px}
.photo-grid{position:absolute;left:42px;top:130px;width:187px;height:225px;display:grid;grid-template-columns:repeat(3,1fr);grid-template-rows:repeat(3,1fr);gap:6px}
.photo-grid__tile{border-radius:1px}
.t1{background:linear-gradient(160deg,#d9b59a,#f1e3d6)}
.t2{background:linear-gradient(160deg,#b78b6c,#e9d3c0)}
.t3{background:linear-gradient(160deg,#d2a98b,#f4ece6)}
.t4{background:linear-gradient(160deg,#9fb3c4,#e8eef2)}
.t5{background:linear-gradient(160deg,#c9a184,#ede0d3)}
.t6{background:linear-gradient(160deg,#a88368,#dcc3ae)}
.t7{background:linear-gradient(160deg,#c7c0c8,#efe8e2)}
.t8{background:linear-gradient(160deg,#8fa7c0,#e2d0c0)}
.t9{background:linear-gradient(160deg,#c19a7c,#f1e6dc)}
.front-panel__bar{position:absolute;left:0;bottom:0;width:268px;height:31px;background:var(--blue);color:var(--white);font-family:Arimo,sans-serif;font-size:10px;display:flex;align-items:center;justify-content:center}

/* inside spread */
.inside-header{position:absolute;left:0;top:0;width:550px;height:56px;background:var(--blue)}
.inside-header__title{position:absolute;left:22px;top:5px;color:var(--white);font-family:Arimo,sans-serif;font-weight:700;font-size:12px;line-height:14.2px}
.inside-header__photo{position:absolute;left:205px;top:0;width:147px;height:56px;background:linear-gradient(90deg,#b9dff2,#f2ece6 45%,#e8c9b4)}
.inside-header__kicker{position:absolute;left:382px;top:20px;color:var(--white);font-family:Arimo,sans-serif;font-weight:700;font-size:13.5px}
.inside-footer{position:absolute;left:0;bottom:0;width:550px;height:8px;background:var(--blue)}
.column{position:absolute;top:64px;font-family:"Didact Gothic",sans-serif;font-size:6.9px;line-height:8.9px;color:var(--ink)}
.column--left{left:34px;width:252px}
.column--right{left:306px;width:238px}
.column p{margin-bottom:8.9px}
.column p.tight{margin-bottom:0}
.column h3{font-family:Arimo,sans-serif;font-weight:700;font-size:6.9px;line-height:8.9px}
.column .stress{font-weight:700;text-decoration:underline}
</style>
</head>
<body>
<main class="canvas">

  <section class="spread spread--cover" aria-label="Brochure outside spread">
    <div class="back-panel">
      <div class="back-panel__accent"></div>
      <address class="contact">
        <div class="contact__name">Martin R. Pike, D.M.D., M.A.G.D., F.I.C.O.I.</div>
        <div>Briar Ridge Dental Care</div>
        <div>418 North Cedar Avenue</div>
        <div>Briar Ridge, PA 17943</div>
        <div>717-829-4617</div>
      </address>
      <div class="contact__url">www.briarridgedentalcare.example</div>
    </div>

    <div class="front-panel">
      <div class="brand">
        <span class="brand__dot"></span>
        <span class="brand__name">Briar Ridge Dental Care</span>
      </div>
      <div class="photo-grid">
        <div class="photo-grid__tile t1" role="img" aria-label="Smiling young woman"></div>
        <div class="photo-grid__tile t2" role="img" aria-label="Smiling man"></div>
        <div class="photo-grid__tile t3" role="img" aria-label="Close-up of a bright smile"></div>
        <div class="photo-grid__tile t4" role="img" aria-label="Dental instruments"></div>
        <div class="photo-grid__tile t5" role="img" aria-label="Smiling woman"></div>
        <div class="photo-grid__tile t6" role="img" aria-label="Mother and child smiling"></div>
        <div class="photo-grid__tile t7" role="img" aria-label="Close-up of healthy teeth"></div>
        <div class="photo-grid__tile t8" role="img" aria-label="Smiling boy brushing teeth"></div>
        <div class="photo-grid__tile t9" role="img" aria-label="Smiling senior couple"></div>
      </div>
      <div class="front-panel__bar">www.briarridgedentalcare.example</div>
    </div>
  </section>

  <section class="spread spread--inside" aria-label="Brochure inside spread">
    <header class="inside-header">
      <h1 class="inside-header__title">3 Dangers of Tooth Loss and<br>Poor Fitting Dentures<br>That You Must Know About!</h1>
      <div class="inside-header__photo" role="img" aria-label="Close-up of a woman's smile"></div>
      <h2 class="inside-header__kicker">Did you know...</h2>
    </header>

    <article class="column column--left">
      <p class="tight">Danger #1</p>
      <p>Bone Loss Makes You Look Older Quicker</p>
      <p>Dental Implants assist you in looking and feeling younger, because they prevent bone loss. By preventing bone loss that would normally occur with the loss of teeth, your facial structure remains normal and intact. The chances of wrinkling and aging before your time is less likely to happen.<br>In other words, every day that you continue to wear dentures you are experiencing bone loss, which makes you look much older than you have to.</p>
      <p class="tight">Danger #2</p>
      <p>Dentures Increase Your Risk of Heart Disease and Oral Cancer</p>
      <p>While tooth loss may seem like a small problem compared with other health and fitness issues, it is often the first sign of bigger health problems for many people and can put them at higher risk for heart disease and oral cancer.<br>When dentures don't fit properly, or are not removed daily, it can lead to bone disease and oral cancer. The National Oral Health Council reports that there will be approximately 30,000 new cases of oral cancer this year alone.<br>Heart disease has been linked to gum disease. When dentures do not fit correctly, you have a higher chance of oral problems. You must be aware of these concerns because dentures can cause more problems than just discomfort and a poor smile.</p>
      <p class="tight">Danger #3</p>
      <p>Dentures May Reduce Your Life Span</p>
      <p>It's True! Many people with poor fitting dentures or multiple missing back teeth live up to 10 years less. This is due to poor eating habits and stomach problems. Denture wearers tend to eat more processed foods and experience other health problems related to poor eating habits. People today now have alternatives to dentures, and the best solution is dental implants.<br>People who get dental implants can finally eat the healthy foods they have been missing such as; apples, fresh vegetables, corn on the cob, and even steak!</p>
    </article>

    <article class="column column--right">
      <p>The quality of your smile has a more direct affect on your life than any other part of your appearance?<br>In fact, 88% of all people in North America say they always remember someone with an especially attractive smile. Not only that, 75% agree an unattractive smile can seriously hurt a person's chance for financial success. Perhaps that's why more than half the adults in America wish they could change their smile. Many people want to rid themselves of their frustrating ill-fitting dentures. Some adults want to correct problems they have had since childhood like discolored, crooked or irregularly shaped teeth. Others want to fix conditions they've developed over time, like cracked, worn-down and discolored teeth. There is a good reason for this. You see...</p>
      <h3>Your Smile Can Make Or Break You!</h3>
      <p>For hundreds of years, all the way from Mona Lisa to today's cover girls, a dazzling smile has always carried great significance. It is an indication of a person's sense of well-being and has an enormous impact on a person's health, self-esteem, as well as personal and business relationships. In short...a beautiful smile makes people more attracted to you, and more eager to do business with you.<br>So, if a smile is so important, why don't more people smile?...and... why don't they smile more often?</p>
      <h3>The answer is simple:</h3>
      <p>Many people are ashamed and embarrassed by their teeth or dentures!</p>
      <h3>Are You A Denture Sufferer?</h3>
      <p>There are many reasons people don't like the appearance of their teeth or dentures: many people are still using old and ill-fitted dentures or partials that pop up, fly out, or get stuck while they are eating or smiling. Some people have teeth too small, to large or crooked. Others have teeth that are gapped or overlapped. Their teeth suffer from stains and discoloration. Some people wear patial or full mouth dentures that don't even fit correctly. Some are crooked, chipped, broken and worn down. And almost everyone wishes their teeth would <span class="stress">fit better, be whiter and look more attractive!</span></p>
      <p>That's the bad news. The good news is every single one of these problems can now be corrected at Briar Ridge Dental Care. Read on to find out how!</p>
    </article>

    <div class="inside-footer"></div>
  </section>

</main>
</body>
</html>
```